Fitness Product bundle graphic needed

I'm currently selling a bundle which consists of a set of exercise bands and access to a related video workout series (it's a set of 3 videos). So I'm looking for a professional graphic that shows this bundle together.

This graphic will be used as the product image in my online store and on possible landing pages.

The important thing is to show off the bands and some sort of representation of the videos in a cool way. Including the carry bag is optional.

I've attached some band pictures, and some screenshots of the videos themselves.

I am open to designs that don't use the attached pictures where it would require me to take new ones. But please include a sample so I would know what kind of pose/picture to take.

fitness and health market

Fitness Equipment

Sans Serif

3277b5
33a6d7

• Be able to swap out the video images easily so I can create different bundles for different video series
• I don't want the videos to look like it's a physical product like it comes with DVDs or in a software box. Since the videos are online only

```html
<!DOCTYPE html>
<html lang="en">
<head>
<meta charset="utf-8">
<title>Fitness Bundle</title>
<link rel="stylesheet" href="https://fonts.googleapis.com/css2?family=Bungee&family=Fjalla+One&family=Roboto:wght@700&display=swap">
<style>
  :root {
    --bg: #e7e4e2;
    --blue-light: #33a6d7;
    --blue-dark: #3277b5;
    --ink: #3a3a3a;
    --room-top: #f4f3f1;
    --room-floor: #6b4a32;
    --band-green: #92d150;
    --band-blue: #1f5fa8;
    --band-yellow: #f2cd1c;
    --band-red: #dc2a23;
    --band-black: #1c1c1c;
    --bag: #141414;
    --gold: #c9a24a;
  }
  * { box-sizing: border-box; margin: 0; padding: 0; }
  html, body { width: 1200px; height: 927px; overflow: hidden; background: var(--bg); }
  .canvas { position: relative; width: 1200px; height: 927px; background: var(--bg); overflow: hidden; }

  .video-thumb {
    position: absolute; left: 55px; width: 468px;
    background: linear-gradient(to bottom, var(--room-top) 0%, #ebe9e6 72%, var(--room-floor) 73%, #5a3c28 100%);
  }
  .video-thumb.one { top: 46px; height: 263px; }
  .video-thumb.two { top: 332px; height: 261px; }
  .video-thumb.three { top: 618px; height: 265px; }
  .thumb-brand {
    position: absolute; left: 22px; top: 14px;
    font-family: "Fjalla One", sans-serif; font-size: 17px; color: var(--blue-dark);
  }
  .play-button { position: absolute; left: 50%; top: 50%; width: 72px; height: 72px; transform: translate(-50%, -50%); }

  .headline {
    position: absolute; left: 500px; top: 14px; width: 800px;
    font-family: "Bungee", sans-serif; font-size: 136px; line-height: 144px;
    color: var(--blue-light); text-align: center; font-weight: 400;
    text-shadow: 2px 2px 0 var(--blue-dark), 4px 4px 0 var(--blue-dark), 6px 6px 0 var(--blue-dark);
    white-space: nowrap;
  }
  .headline .word { display: block; transform: scaleX(0.68); transform-origin: center; }
  .subline {
    position: absolute; left: 600px; top: 302px; width: 600px;
    font-family: "Fjalla One", sans-serif; font-size: 34px; line-height: 32px;
    color: var(--ink); text-align: center; text-transform: uppercase; letter-spacing: 0.3px;
  }

  .band { position: absolute; top: 390px; height: 474px; width: 80px; }
  .band.green { left: 620px; width: 100px; background: var(--band-green); }
  .band.blue { left: 748px; background: var(--band-blue); }
  .band.yellow { left: 852px; background: var(--band-yellow); }
  .band.red { left: 956px; background: var(--band-red); }
  .band.black { left: 1060px; width: 108px; top: 386px; height: 494px; background: var(--band-black); }
  .band-rating {
    position: absolute; left: 0; right: 0; bottom: 40px; text-align: center;
    font-family: "Roboto", Arial, sans-serif; font-weight: 700; font-size: 13px; color: #fff;
  }
  .dots { display: flex; justify-content: center; gap: 4px; margin-bottom: 12px; }
  .dots span { width: 9px; height: 9px; border-radius: 50%; background: #fff; }
  .dots span.off { background: transparent; border: 1.5px solid #fff; }

  .carry-bag { position: absolute; left: 600px; top: 600px; width: 280px; height: 290px; }
  .bag-brand {
    position: absolute; left: 700px; top: 752px; transform: rotate(-20deg);
    font-family: "Fjalla One", sans-serif; color: var(--gold); text-align: center;
  }
  .bag-brand .name { font-size: 18px; }
  .bag-brand .url { font-size: 8px; margin-top: 6px; }
</style>
</head>
<body>
<main class="canvas">
  <section class="video-thumb one" role="img" aria-label="Video still: woman seated on a chair doing a band exercise in a bright room">
    <span class="thumb-brand">Flexora</span>
    <svg class="play-button" viewBox="0 0 72 72"><circle cx="36" cy="36" r="32" fill="rgba(255,255,255,0.25)" stroke="#000" stroke-width="5"/><path d="M28 22 L50 36 L28 50 Z" fill="#000"/></svg>
  </section>
  <section class="video-thumb two" role="img" aria-label="Video still: man doing a glute bridge with a band on a blue mat">
    <span class="thumb-brand">Flexora</span>
    <svg class="play-button" viewBox="0 0 72 72"><circle cx="36" cy="36" r="32" fill="rgba(255,255,255,0.25)" stroke="#000" stroke-width="5"/><path d="M28 22 L50 36 L28 50 Z" fill="#000"/></svg>
  </section>
  <section class="video-thumb three" role="img" aria-label="Video still: woman standing on one leg with a band on a white mat">
    <span class="thumb-brand">Flexora</span>
    <svg class="play-button" viewBox="0 0 72 72"><circle cx="36" cy="36" r="32" fill="rgba(255,255,255,0.25)" stroke="#000" stroke-width="5"/><path d="M28 22 L50 36 L28 50 Z" fill="#000"/></svg>
  </section>

  <h1 class="headline"><span class="word">FITNESS</span><span class="word">BUNDLE</span></h1>
  <p class="subline">Bundle includes exercise bands,<br>&nbsp;and 3 set fitness of videos.</p>

  <div class="band green" role="img" aria-label="Green light resistance band"></div>
  <div class="band blue" role="img" aria-label="Blue resistance band"></div>
  <div class="band yellow" role="img" aria-label="Yellow medium resistance band">
    <div class="band-rating"><div class="dots"><span></span><span></span><span></span><span class="off"></span><span class="off"></span></div>Medium</div>
  </div>
  <div class="band red" role="img" aria-label="Red heavy resistance band">
    <div class="band-rating"><div class="dots"><span></span><span></span><span></span><span></span><span class="off"></span></div>Heavy</div>
  </div>
  <div class="band black" role="img" aria-label="Black extra heavy resistance band">
    <div class="band-rating"><div class="dots"><span></span><span></span><span></span><span></span><span></span></div>X-Heavy</div>
  </div>

  <svg class="carry-bag" viewBox="0 0 280 290" role="img" aria-label="Black drawstring carry bag">
    <path d="M70 70 L200 40 L270 240 L120 290 L0 230 Z" fill="var(--bag)"/>
    <path d="M150 55 C180 10 240 0 250 40 C255 70 220 80 200 60" fill="none" stroke="var(--bag)" stroke-width="3"/>
  </svg>
  <div class="bag-brand"><div class="name">Flexora</div><div class="url">www.flexora-fit.com</div></div>
</main>
</body>
</html>
```